Elegant and modern Wedding Photography brochure

My existing brochure (attached) needs a major facelift. This is one of the main selling tools - it gets emailed to my clients when they make an equiry on what packages i offer and it is printed out and walked through at our first meeting. This brochure is as critical as my website - it needs to sing!

I'm looking for an eye-catching design that says:
Elegant
Modern
Clean
Crisp
Not cutesy or lovey-dovey thanks - we are more sophisticated and professional than that.

Update images to some of the latest weddings I've shot also. Let me know files and resolution you need. I've enabled right-click to download images on my site for a limited time. Please note that I retain copyright and will pursue any breeches.

Http://www.carlathornbey.com/Melbourne-wedding-photography
Updates

Thanks for all of your designs! Will take a few days to decide.

Target Market(s)

Australian Women aged 24-44

Industry/Entity Type

Wedding

Font styles to use
Other font styles liked:
• Century Gothic

Requirements
Must have
• Easy to print - does not have to be 6 A4 pages like the existing brochure
Nice to have
• Some full page images - The photos are supposed to be the hero here :-)
Should not have
• Not cutesy or lovey-dovey thanks - we are more sophisticated and professional than that.

No black backgrounds, I prefer a white thanks

No images in organic shaped boxes (like the rectangles in the logo - no thanks).
Keep the lines straight and sharp

```html
<!DOCTYPE html>
<html lang="en">
<head>
<meta charset="utf-8">
<title>Wedding Packages</title>
<link href="https://fonts.googleapis.com/css2?family=Didact+Gothic&display=swap" rel="stylesheet">
<style>
  :root {
    --plum: #8c2a85;
    --blush: #f4b5d2;
    --blush-text: #f6bcd9;
    --body-grey: #7a7a7a;
    --white: #ffffff;
  }
  * { box-sizing: border-box; margin: 0; padding: 0; }
  html, body { width: 1200px; height: 852px; overflow: hidden; background: var(--white); }
  body { font-family: "Didact Gothic", "Century Gothic", sans-serif; position: relative; }

  .page-header {
    position: absolute; left: 0; top: 0; width: 1200px; height: 103px;
    background: var(--plum);
  }
  .page-title {
    position: absolute; left: 0; right: 0; top: 28px;
    text-align: center; line-height: 1;
    color: var(--blush-text); font-weight: 400; font-size: 50px;
  }

  .packages { position: absolute; left: 0; top: 103px; width: 1200px; display: flex; }
  .package { width: 400px; }
  .package-photo { display: block; width: 100%; height: 265px; }
  .photo-signature { background: linear-gradient(135deg, #6f6a3a 0%, #a89b63 45%, #8b7a55 100%); }
  .photo-platinum { background: linear-gradient(180deg, #3d4a2c 0%, #6a7448 50%, #8a5a3a 100%); }
  .photo-gold { background: linear-gradient(135deg, #7a6a58 0%, #a8957a 50%, #d8d2c8 100%); }

  .package-name {
    height: 40px; line-height: 40px; text-align: center;
    color: var(--white); font-size: 24px; font-weight: 400;
  }
  .name-light { background: var(--blush); }
  .name-dark { background: var(--plum); }

  .package-details { padding: 11px 0 0 65px; }
  .price { color: var(--plum); font-size: 17.5px; line-height: 24px; margin-bottom: 4px; }
  .coverage { color: var(--body-grey); font-size: 14px; line-height: 19px; margin-bottom: 9px; }
  .inclusions { list-style: none; }
  .inclusions li {
    position: relative; color: var(--body-grey); font-size: 14px; line-height: 19px;
    margin-bottom: 9px; white-space: nowrap;
  }
  .inclusions li::before {
    content: ""; position: absolute; left: -14px; top: 7px;
    width: 4px; height: 4px; border-radius: 50%; background: var(--plum);
  }

  .footnote {
    position: absolute; left: 441px; top: 801px;
    color: var(--blush); font-size: 10.5px; white-space: nowrap;
  }
  .page-number {
    position: absolute; right: 10px; top: 752px;
    color: var(--blush); font-size: 112px; line-height: 1;
  }
</style>
</head>
<body>
  <header class="page-header">
    <h1 class="page-title">Wedding Packages</h1>
  </header>

  <main class="packages">
    <section class="package">
      <div class="package-photo photo-signature" role="img" aria-label="Bride and groom posed among willow trees"></div>
      <h2 class="package-name name-light">Signature</h2>
      <div class="package-details">
        <p class="price">Price: $3650 &nbsp;($5540 value)</p>
        <p class="coverage">Up to 8 hrs of coverage</p>
        <ul class="inclusions">
          <li>Signature Grand (A3) Album with<br>Lay-flat 300g paper, frosted page,<br>choice of premium linen or leather<br>cover, presentation box, name<br>embossing, up to 52 pages</li>
          <li>Custom Thank-you Cards with<br>envelopes (50)</li>
          <li>Client for life (no sitting fees)</li>
          <li>Second photographer</li>
          <li>Fusion Slideshow (still + moving images)</li>
          <li>Pre-wedding Shoot</li>
          <li>Web Gallery (online for 6 weeks) &amp;<br>Social media</li>
          <li>High Resolution Digital Negatives*</li>
        </ul>
      </div>
    </section>

    <section class="package">
      <div class="package-photo photo-platinum" role="img" aria-label="Couple kissing on a tree-lined avenue in autumn"></div>
      <h2 class="package-name name-dark">Platinum</h2>
      <div class="package-details">
        <p class="price">Price: $2300 &nbsp;($3440 value)</p>
        <p class="coverage">Up to 6 hrs of coverage</p>
        <ul class="inclusions">
          <li>Regular (A4) Album with Lay-flat 300g<br>paper, printed cover, dust jacket,<br>presentation box, up to 42 pages</li>
          <li>Slideshow</li>
          <li>Pre-wedding shoot</li>
          <li>Web Gallery (online for 6 weeks) &amp;<br>Social media</li>
          <li>High Resolution Digital Negatives*</li>
        </ul>
      </div>
    </section>

    <section class="package">
      <div class="package-photo photo-gold" role="img" aria-label="Bride and groom in front of a bluestone church"></div>
      <h2 class="package-name name-light">Gold</h2>
      <div class="package-details">
        <p class="price">Price: $1650 &nbsp;($2080 value)</p>
        <p class="coverage">Up to 4 hrs of coverage</p>
        <ul class="inclusions">
          <li>Regular (A4) Album with Lay-flat 300g<br>paper, printed cover, dust jacket,<br>presentation box, up to 32 pages</li>
          <li>Web Gallery (online for 6 weeks) &amp;<br>Social media</li>
          <li>High Resolution Digital Negatives*</li>
        </ul>
      </div>
    </section>
  </main>

  <p class="footnote">* Approx. 1200x1800 jpeg at 240 pixels per inch. Suitable for prints up to 8x10inch. No watermarks</p>
  <p class="page-number">4</p>
</body>
</html>
```